Business Card Design Project- Removalist

I would like to surprise my husband to be with a different type of wedding present. His brother (who he owned a removalist business with) suddenly passed away from cancer recently and he has changed his business name to 'RTB' (which stands for Raising Tom Bright; but the full name doesn't need to be on the business card as it is more of a personal business name). To celebrate the new business I would like to get him some business cards made.
I would like the business name to be listed as 'RTB' and somewhere on the card I would like 'Sydney wide removals and relocation services'. I would like it to be obvious from the front of the card that it is a removalist business card. If a truck or some other feature that makes it look like a removalist business card could added it would be appreciated.
I don't mind what colours are used, but I would like the colour blue to feature somewhere in the design. It can be bright and fun, which is how Tom was.
I will also need the company's email address and phone number listed
The email address is: rtbremovals@quillpost.example
The contact number is: 0417 282 934
I don't need a contact name listed on the card, but perhaps 'Owned and operated by the Pendleworth family' could be added near the contact details in small font.
Thank you very much for considering this project!
Kind regards,
Fiona
Updates
Could you please change the mobile contact number to 0417 282 934. This is the only contact phone number required on the card now.
Thank you!

```html
<!DOCTYPE html>
<html lang="en">
<head>
<meta charset="utf-8">
<title>RTB Business Cards</title>
<link href="https://fonts.googleapis.com/css2?family=Jost:wght@400;500&family=Arimo:wght@400&display=swap" rel="stylesheet">
<style>
  :root {
    --backdrop: #141414;
    --navy: #253a7e;
    --mid-blue: #0a6ab0;
    --brand-blue: #21448f;
    --caption-blue: #1a5a8c;
    --white: #ffffff;
    --photo-warm: #c99a55;
    --photo-light: #eee9e0;
    --photo-deep: #8a6a3c;
  }
  * { box-sizing: border-box; margin: 0; padding: 0; }
  html, body {
    width: 1200px; height: 722px; overflow: hidden;
    background: var(--backdrop);
  }
  .stage { position: relative; width: 1200px; height: 722px; }
  .card {
    position: absolute; width: 514px; height: 294px;
    border-radius: 12px; overflow: hidden;
    background: var(--white);
    border: 2px solid var(--white);
  }
  .band {
    position: absolute; left: 0; right: 0;
    background: linear-gradient(90deg, var(--navy) 0%, var(--mid-blue) 55%, var(--navy) 100%);
  }
  .wordmark {
    position: absolute; font-family: 'Jost', sans-serif; font-weight: 500;
    line-height: 1; letter-spacing: 2px;
  }

  /* Front */
  .card-front { left: 73px; top: 43px; }
  .card-front .band { top: 166px; bottom: 0; }
  .owner-line {
    position: absolute; top: 19px; width: 100%; text-align: center;
    font-family: 'Jost', sans-serif; font-size: 21px; color: var(--caption-blue);
  }
  .card-front .wordmark {
    top: 75px; left: 0; width: 100%; text-align: center;
    font-size: 112px; color: var(--brand-blue);
  }
  .service-line {
    position: absolute; top: 175px; width: 100%; text-align: center;
    font-family: 'Arimo', sans-serif; font-size: 17px; color: var(--white);
  }
  .contacts {
    position: absolute; top: 230px; width: 100%;
    display: flex; justify-content: center; gap: 26px;
    font-family: 'Jost', sans-serif; font-size: 17px; color: var(--white);
  }
  .contact { display: flex; align-items: center; gap: 7px; }
  .contact svg { width: 15px; height: 15px; fill: var(--white); }

  /* Back */
  .card-back { left: 613px; top: 43px; }
  .card-back .band { top: 0; height: 166px; }
  .card-back .wordmark {
    top: 78px; left: 0; width: 100%; text-align: center;
    font-size: 108px; color: var(--white);
  }

  /* Lifestyle card */
  .card-photo { left: 378px; top: 375px; border: none; }
  .photo-fill {
    position: absolute; inset: 0;
    background:
      linear-gradient(180deg, var(--photo-light) 0%, rgba(238,233,224,0) 35%),
      linear-gradient(160deg, var(--photo-light) 0%, var(--photo-warm) 45%, var(--photo-deep) 75%, var(--photo-light) 100%);
  }
  .card-photo .wordmark {
    top: 26px; left: 26px; font-size: 80px; color: var(--brand-blue);
  }
</style>
</head>
<body>
<div class="stage">

  <section class="card card-front">
    <p class="owner-line">Owned and operated by the Pendleworth family</p>
    <div class="band"></div>
    <span class="wordmark">RTB</span>
    <p class="service-line">Sydney Wide Removals &amp; Relocation Services</p>
    <div class="contacts">
      <span class="contact">
        <svg viewBox="0 0 24 24"><path d="M6.6 10.8a15.1 15.1 0 0 0 6.6 6.6l2.2-2.2a1 1 0 0 1 1-.25 11.4 11.4 0 0 0 3.6.57 1 1 0 0 1 1 1V20a1 1 0 0 1-1 1A17 17 0 0 1 3 4a1 1 0 0 1 1-1h3.5a1 1 0 0 1 1 1c0 1.25.2 2.45.57 3.57a1 1 0 0 1-.25 1z"/></svg>
        0417 282 934
      </span>
      <span class="contact">
        <svg viewBox="0 0 24 24"><path d="M2 9l10-6 10 6v11H2z M4 10l8 5 8-5"/><path d="M4 10l8 5 8-5v9H4z" fill="#0a6ab0"/></svg>
        rtbremovals@quillpost.example
      </span>
    </div>
  </section>

  <section class="card card-back">
    <div class="band"></div>
    <span class="wordmark">RTB</span>
  </section>

  <section class="card card-photo">
    <div class="photo-fill" role="img" aria-label="Photo of a couple relaxing on a tan sofa among open moving boxes and packing paper in a bright new home"></div>
    <span class="wordmark">RTB</span>
  </section>

</div>
</body>
</html>
```